Cocktail-Making Assistant App re-design

Ok boys and girls, here's the deal:
I have an android app which is almost complete, but needs a design overhaul.

The app is a standard cocktail-making assistant: gives you a list of cocktails and the ability to see which cocktail you can make out of those ingredients (drinks, fruit, etc) you have at home.

I've attached some general app flow, as well as detailed requirements/explanation presentation. Most of those things are just FYI, so that you know what it's about.

3 screens are the most important (main screen, cocktail view screen, ingredient view screen), meaning I will pick the design mostly based on ideas for those 3 things, with the fourth being a rather simple list (given on attached flow, third tier)
Some other screens are derived from that, with some minor changes on it, but you shouldn't care about that.

There are lots of other, non-explained things which I said nothing about only because they are (from design point of view) completely the same and would only make it seem more complicated.

I don't want to influence the colour scheme, but the app will be released under RedFern developer name (having a light colured red fern as a logo) so I suppose some brownish design, for example, will not really fit nicely. If you, however, have a killer which you are confident will prove me wrong, I'm looking forward to seeing it!

It should be a serious, elegant look (as opposed to cartoonish, but we are not aiming for a business look at all!), not cluttered with details, no clubbing themes, glitter and so on.

Test apk file available on request (Android 2.3+).

Edit: payment is now guaranteed
Also please note that currently, the favorite, "heart" button has a motion effect:
on click it flies out of the screen to the left (white heart) and comes back to the screen as a red heart. Take that into consideration, if it means anything to you.
Updates

Target Market(s)

Whoever you imagine would enjoy drinking cocktails

Industry/Entity Type

Business

Requirements
Must have
• Everything is said in the provided documentation - images say more than I could possibly write here.
Nice to have
• As said, most of the icons are a nice-to-have. Only those which are critically linked to the rest of the design must be provided. More details in the docs.
Should not have
• No cartoon look, No zillion colours

```html
<!DOCTYPE html>
<html lang="en">
<head>
<meta charset="utf-8">
<title>Cocktail Assistant – Main Screen</title>
<link rel="stylesheet" href="https://fonts.googleapis.com/css2?family=Michroma&display=swap">
<style>
  :root {
    --ink: #2f2f2f;
    --bar-top: #ffffff;
    --bar-bottom: #ebebeb;
    --divider: #d6d6d6;
    --tile-mixer: #aed577;
    --tile-bar: #fdb660;
    --tile-menu: #fc5c63;
    --tile-favourites: #d0afa6;
    --tile-shop: #fee672;
    --tile-awards: #b1a8eb;
    --gutter: #ffffff;
  }
  * { box-sizing: border-box; margin: 0; padding: 0; }
  html, body { width: 676px; height: 1200px; overflow: hidden; background: var(--gutter); }
  .screen { width: 676px; height: 1200px; display: flex; flex-direction: column; }

  .top-bar {
    position: relative; z-index: 2;
    height: 97px; flex: none;
    display: grid; grid-template-columns: 131px 283px 131px 131px;
    background: linear-gradient(var(--bar-top), var(--bar-bottom));
    box-shadow: 0 4px 4px rgba(0,0,0,.35);
  }
  .top-bar__item {
    display: flex; align-items: center; justify-content: center;
    border-left: 1px solid var(--divider);
  }
  .top-bar__item:first-child { border-left: none; }
  .points {
    font-family: "Michroma", sans-serif;
    font-size: 26px; letter-spacing: 1px; color: #111;
    white-space: nowrap;
  }

  .tiles {
    flex: 1;
    display: grid;
    grid-template-columns: 1fr 1fr;
    grid-template-rows: repeat(3, 1fr);
    column-gap: 2px;
    padding-top: 6px;
    background: var(--gutter);
  }
  .tile { display: block; }
  .tile svg { width: 100%; height: 100%; display: block; }
  .tile--mixer { background: var(--tile-mixer); }
  .tile--bar { background: var(--tile-bar); }
  .tile--menu { background: var(--tile-menu); }
  .tile--favourites { background: var(--tile-favourites); }
  .tile--shop { background: var(--tile-shop); }
  .tile--awards { background: var(--tile-awards); }
</style>
</head>
<body>
<main class="screen">
  <header class="top-bar">
    <div class="top-bar__item home-button" aria-label="Home">
      <svg width="54" height="52" viewBox="0 0 54 52">
        <path d="M27 2 L2 25 H9 V50 H22 V34 H32 V50 H45 V25 H52 Z" fill="#111"/>
        <rect x="39" y="5" width="6" height="12" fill="#111"/>
      </svg>
    </div>
    <div class="top-bar__item">
      <span class="points">PONTS : 100</span>
    </div>
    <div class="top-bar__item menu-button" aria-label="Menu">
      <svg width="48" height="36" viewBox="0 0 48 36">
        <rect x="0" y="0" width="48" height="7" rx="3" fill="#111"/>
        <rect x="0" y="14" width="48" height="7" rx="3" fill="#111"/>
        <rect x="0" y="28" width="48" height="7" rx="3" fill="#111"/>
      </svg>
    </div>
    <div class="top-bar__item settings-button" aria-label="Settings">
      <svg width="46" height="44" viewBox="0 0 46 44">
        <g fill="#111">
          <circle cx="16" cy="28" r="10"/>
          <g transform="translate(16 28)">
            <rect x="-3" y="-15" width="6" height="30"/>
            <rect x="-15" y="-3" width="30" height="6"/>
            <rect x="-3" y="-15" width="6" height="30" transform="rotate(45)"/>
            <rect x="-3" y="-15" width="6" height="30" transform="rotate(-45)"/>
          </g>
          <circle cx="33" cy="11" r="6"/>
          <g transform="translate(33 11)">
            <rect x="-2" y="-10" width="4" height="20"/>
            <rect x="-10" y="-2" width="20" height="4"/>
            <rect x="-2" y="-10" width="4" height="20" transform="rotate(45)"/>
            <rect x="-2" y="-10" width="4" height="20" transform="rotate(-45)"/>
          </g>
        </g>
        <circle cx="16" cy="28" r="4" fill="#f4f4f4"/>
        <circle cx="33" cy="11" r="2.5" fill="#f4f4f4"/>
      </svg>
    </div>
  </header>

  <nav class="tiles">
    <a class="tile tile--mixer" aria-label="Cocktail mixer">
      <svg viewBox="0 0 320 345" preserveAspectRatio="xMidYMid meet">
        <path d="M148 43 H162 L172 60 H138 Z" fill="var(--ink)"/>
        <path d="M138 60 H172 L214 98 V112 L210 116 H106 L102 112 V98 Z" fill="var(--ink)"/>
        <path d="M108 119 H212 L193 237 H132 Z" fill="var(--ink)"/>
      </svg>
    </a>
    <a class="tile tile--bar">
      <svg viewBox="0 0 320 345" preserveAspectRatio="xMidYMid meet">
        <rect x="52" y="40" width="230" height="200" rx="14" fill="#d9954a" role="img" aria-label="Icon of a seated guest at a table with a beer mug"/>
      </svg>
    </a>
    <a class="tile tile--menu">
      <svg viewBox="0 0 320 345" preserveAspectRatio="xMidYMid meet">
        <rect x="45" y="43" width="217" height="145" rx="10" fill="#d9464d" role="img" aria-label="Icon of an open drinks menu with bottles and a glass"/>
      </svg>
    </a>
    <a class="tile tile--favourites" aria-label="Add favourite">
      <svg viewBox="0 0 320 345" preserveAspectRatio="xMidYMid meet">
        <path d="M144 205 L70 120 C40 86 60 45 100 45 C124 45 138 60 144 74 C150 60 166 45 190 45 C230 45 250 86 220 120 Z" fill="var(--ink)" stroke-linejoin="round"/>
        <circle cx="225" cy="155" r="63" fill="var(--tile-favourites)"/>
        <circle cx="225" cy="155" r="52" fill="var(--ink)"/>
        <rect x="197" y="150" width="56" height="10" rx="5" fill="var(--tile-favourites)"/>
        <rect x="220" y="127" width="10" height="56" rx="5" fill="var(--tile-favourites)"/>
      </svg>
    </a>
    <a class="tile tile--shop" aria-label="Shopping list">
      <svg viewBox="0 0 320 345" preserveAspectRatio="xMidYMid meet">
        <path d="M56 58 H92 L118 160 H222 L242 98" fill="none" stroke="var(--ink)" stroke-width="22" stroke-linecap="round" stroke-linejoin="round"/>
        <g transform="rotate(30 170 100)">
          <rect x="158" y="80" width="26" height="66" rx="6" fill="var(--ink)"/>
          <rect x="165" y="58" width="12" height="24" fill="var(--ink)"/>
          <rect x="164" y="48" width="14" height="8" fill="var(--ink)"/>
        </g>
        <circle cx="133" cy="210" r="20" fill="var(--ink)"/>
        <circle cx="200" cy="210" r="20" fill="var(--ink)"/>
      </svg>
    </a>
    <a class="tile tile--awards" aria-label="Achievements">
      <svg viewBox="0 0 320 345" preserveAspectRatio="xMidYMid meet">
        <polygon points="125,150 160,180 120,235 112,200 85,200" fill="var(--ink)"/>
        <polygon points="245,150 210,180 250,235 258,200 285,200" fill="var(--ink)"/>
        <polygon transform="translate(185 100)" fill="var(--ink)" stroke="var(--ink)" stroke-width="5" stroke-linejoin="round"
          points="56,0 44.4,11.9 48.5,28 32.5,32.5 28,48.5 11.9,44.4 0,56 -11.9,44.4 -28,48.5 -32.5,32.5 -48.5,28 -44.4,11.9 -56,0 -44.4,-11.9 -48.5,-28 -32.5,-32.5 -28,-48.5 -11.9,-44.4 0,-56 11.9,-44.4 28,-48.5 32.5,-32.5 48.5,-28 44.4,-11.9"/>
      </svg>
    </a>
  </nav>
</main>
</body>
</html>
```